Roofing Company Sales Rep Business Card

Business card for sales rep to canvass and hand out to property owners/managers for free roof inspections and roof replacements.

```html
<!DOCTYPE html>
<html lang="en">
<head>
<meta charset="utf-8">
<title>Ridgeline Roofing – Sales Representative Card</title>
<link rel="stylesheet" href="https://fonts.googleapis.com/css2?family=Montserrat:wght@400;500;700;800&display=swap">
<style>
  :root {
    --page-bg: #e4e4e6;
    --card-white: #f7f7f7;
    --card-black: #07090a;
    --brand-red: #d3191f;
    --ink: #1a1a1a;
    --ink-soft: #2b2b2b;
    --white: #ffffff;
  }
  * { box-sizing: border-box; margin: 0; padding: 0; }
  html, body {
    width: 1200px; height: 1200px; overflow: hidden;
    background: var(--page-bg);
    font-family: "Montserrat", Arial, sans-serif;
  }
  .sheet {
    width: 1200px; height: 1200px;
    display: flex; flex-direction: column; align-items: center; justify-content: center;
    gap: 60px;
  }
  .card {
    position: relative;
    width: 700px; height: 400px;
    border-radius: 4px;
    overflow: hidden;
    box-shadow: 0 10px 28px rgba(0,0,0,.18);
  }
  /* back */
  .card--back {
    background: radial-gradient(ellipse at 50% 45%, #1a1d1f 0%, var(--card-black) 65%);
    display: flex; align-items: center; justify-content: center;
  }
  .wordmark {
    display: flex; align-items: center; gap: 12px;
    font-weight: 800; letter-spacing: 1px; text-transform: uppercase;
  }
  .wordmark__square { width: 18px; height: 18px; }
  .card--back .wordmark { font-size: 40px; color: var(--white); }
  .card--back .wordmark__square { background: var(--white); width: 24px; height: 24px; }
  /* front */
  .card--front { background: var(--card-white); }
  .card--front .wordmark {
    position: absolute; left: 250px; top: 78px;
    font-size: 30px; color: var(--ink);
  }
  .card--front .wordmark__square { background: var(--brand-red); }
  .contact {
    position: absolute; left: 36px; top: 150px;
    list-style: none; font-size: 15px; color: var(--ink-soft); line-height: 1.5;
  }
  .contact__item { display: flex; align-items: center; gap: 8px; }
  .contact__icon { width: 13px; height: 13px; flex: none; fill: var(--brand-red); }
  .contact__address { margin-top: 2px; }
  .rep {
    position: absolute; left: 420px; top: 185px;
  }
  .rep__name { font-size: 27px; font-weight: 700; color: var(--brand-red); }
  .rep__title { font-size: 16px; font-weight: 400; color: var(--ink-soft); margin-top: 2px; }
  .band { position: absolute; left: 0; top: 0; width: 700px; height: 400px; }
</style>
</head>
<body>
<main class="sheet">
  <section class="card card--back" aria-label="Card back">
    <div class="wordmark"><span class="wordmark__square"></span>Ridgeline Roofing</div>
  </section>

  <section class="card card--front" aria-label="Card front">
    <svg class="band" viewBox="0 0 700 400" aria-hidden="true">
      <path d="M0 300 L265 300 Q285 300 296 292 L304 299 Q292 312 268 312 L0 312 Z" fill="var(--ink)"/>
      <path d="M0 312 L268 312 Q292 312 304 299 Q314 290 334 290 L700 290 L700 400 L0 400 Z" fill="var(--brand-red)"/>
    </svg>

    <div class="wordmark"><span class="wordmark__square"></span>Ridgeline Roofing</div>

    <ul class="contact">
      <li class="contact__item">
        <svg class="contact__icon" viewBox="0 0 16 16"><path d="M3.6 1.2l2.3 2.5-1.3 1.8c.9 2 2.6 3.7 4.6 4.6l1.8-1.3 2.5 2.3-1.4 2.6C7.3 13.5 2.5 8.7 1 3z"/></svg>
        (405)-555-0147
      </li>
      <li class="contact__item">
        <svg class="contact__icon" viewBox="0 0 16 16"><path d="M1 3h14v10H1z M1.8 3.8L8 9l6.2-5.2" stroke="#f7f7f7" stroke-width="1.2"/></svg>
        info@ridgelineroofs.com
      </li>
      <li class="contact__item">
        <svg class="contact__icon" viewBox="0 0 16 16"><circle cx="8" cy="8" r="7"/><path d="M1 8h14M8 1c-3 3.5-3 10.5 0 14M8 1c3 3.5 3 10.5 0 14" stroke="#f7f7f7" stroke-width="1.1" fill="none"/></svg>
        www.ridgelineroofs.com
      </li>
      <li class="contact__address">4780 Cedar Road<br>Millbrook Maine 04021</li>
    </ul>

    <div class="rep">
      <h1 class="rep__name">Marcus Dale</h1>
      <p class="rep__title">sales representative</p>
    </div>
  </section>
</main>
</body>
</html>
```